Paws Of Kindness Business cards

Design a cool, modern business card for my bully breed rescue.

Contact Information for Business Card

Marlene
517-382-4061 Marlene@PawsOfKindnessRescue.net PawsOfKindnessRescue.net

Font styles to use
Serif
Sans Serif

Colors

Designer to choose colors to be used in the design.

Requirements
Must have
• logo and info. Color
Nice to have
• Foil. Maybe some paw prints on the back or some kind of dog illustration.

```html
<!DOCTYPE html>
<html lang="en">
<head>
<meta charset="utf-8">
<title>Paws Of Kindness – Business Cards</title>
<link href="https://fonts.googleapis.com/css2?family=Oswald:wght@600&family=Montserrat:wght@600&family=Open+Sans:wght@500&display=swap" rel="stylesheet">
<style>
  :root {
    --backdrop: #3a3a3a;
    --card-white: #ffffff;
    --charcoal: #3b3a3c;
    --accent-red: #e8303a;
    --soft-grey: #dcdcdc;
    --ink: #161616;
    --contact-text: #ffffff;
  }
  html, body {
    margin: 0;
    padding: 0;
    width: 1200px;
    height: 801px;
    overflow: hidden;
    background: var(--backdrop);
  }
  .canvas {
    position: relative;
    width: 1200px;
    height: 801px;
  }
  .card {
    position: absolute;
    top: 267px;
    width: 450px;
    height: 269px;
    background: var(--card-white);
    overflow: hidden;
    box-shadow: 0 8px 24px rgba(0,0,0,0.5);
  }
  .card--front { left: 133px; }
  .card--back { left: 620px; }
  .card-shapes {
    position: absolute;
    inset: 0;
    width: 450px;
    height: 269px;
  }
  .shape-dark { fill: var(--charcoal); }
  .shape-red { fill: var(--accent-red); }
  .shape-grey { fill: var(--soft-grey); }

  .brand {
    position: absolute;
    display: flex;
    align-items: center;
    gap: 6px;
    font-family: "Oswald", sans-serif;
    font-weight: 600;
    color: var(--ink);
    white-space: nowrap;
  }
  .brand-dot {
    border-radius: 50%;
    background: var(--ink);
    flex: none;
  }
  .card--front .brand {
    left: 14px;
    top: 96px;
    font-size: 21px;
  }
  .card--front .brand-dot { width: 10px; height: 10px; }
  .card--back .brand {
    left: 76px;
    top: 118px;
    font-size: 31px;
    gap: 9px;
  }
  .card--back .brand-dot { width: 14px; height: 14px; }

  .holder-name {
    position: absolute;
    left: 275px;
    top: 47px;
    margin: 0;
    font-family: "Montserrat", sans-serif;
    font-weight: 600;
    font-size: 19px;
    letter-spacing: 1px;
    color: var(--accent-red);
  }
  .contact-list {
    position: absolute;
    left: 252px;
    top: 158px;
    width: 192px;
    margin: 0;
    padding: 0;
    list-style: none;
    font-family: "Open Sans", sans-serif;
    font-weight: 500;
    font-size: 9.5px;
    color: var(--contact-text);
  }
  .contact-list li {
    display: flex;
    align-items: center;
    gap: 5px;
    height: 20px;
    white-space: nowrap;
  }
  .contact-icon {
    width: 11px;
    height: 11px;
    flex: none;
  }
</style>
</head>
<body>
<main class="canvas">

  <section class="card card--front" aria-label="Business card front">
    <svg class="card-shapes" viewBox="0 0 450 269" aria-hidden="true">
      <polygon class="shape-grey" points="236,52 222,150 206,150" />
      <polygon class="shape-dark" points="262,0 450,0 450,269 150,269" />
      <polygon class="shape-red" points="262,0 150,269 128,269 246,36" />
      <polygon class="shape-red" points="168,0 262,0 196,58 214,22" />
    </svg>

    <div class="brand">
      <span class="brand-dot"></span>
      <span class="brand-name">Paws Of Kindness</span>
    </div>

    <h1 class="holder-name">MARLENE</h1>

    <ul class="contact-list">
      <li>
        <svg class="contact-icon" viewBox="0 0 12 12" aria-hidden="true">
          <circle cx="6" cy="6" r="6" fill="var(--accent-red)"/>
          <path d="M4 3.2 L5 3 L5.6 4.6 L4.9 5.1 Q5.5 6.6 6.9 7.1 L7.4 6.4 L9 7 L8.8 8 Q6.5 8.6 4.6 6.6 Q3.2 5 4 3.2Z" fill="#fff"/>
        </svg>
        <span>517-382-4061</span>
      </li>
      <li>
        <svg class="contact-icon" viewBox="0 0 12 12" aria-hidden="true">
          <circle cx="6" cy="6" r="6" fill="var(--accent-red)"/>
          <rect x="3" y="4" width="6" height="4.2" fill="none" stroke="#fff" stroke-width="0.9"/>
          <path d="M3 4 L6 6.3 L9 4" fill="none" stroke="#fff" stroke-width="0.9"/>
        </svg>
        <span>Marlene@PawsOfKindnessRescue.net</span>
      </li>
      <li>
        <svg class="contact-icon" viewBox="0 0 12 12" aria-hidden="true">
          <circle cx="6" cy="6" r="6" fill="var(--accent-red)"/>
          <circle cx="6" cy="6" r="3.2" fill="none" stroke="#fff" stroke-width="0.8"/>
          <path d="M2.8 6 H9.2 M6 2.8 Q4.3 6 6 9.2 M6 2.8 Q7.7 6 6 9.2" fill="none" stroke="#fff" stroke-width="0.7"/>
        </svg>
        <span>PawsOfKindnessRescue.net</span>
      </li>
    </ul>
  </section>

  <section class="card card--back" aria-label="Business card back">
    <svg class="card-shapes" viewBox="0 0 450 269" aria-hidden="true">
      <polygon class="shape-red" points="310,0 418,0 450,22 450,40 396,70 388,44" />
      <polygon class="shape-grey" points="428,62 392,160 404,110" />
      <polygon class="shape-dark" points="450,50 450,269 356,269" />
      <polygon class="shape-red" points="450,36 356,269 336,269 440,48" />
    </svg>

    <div class="brand">
      <span class="brand-dot"></span>
      <span class="brand-name">Paws Of Kindness</span>
    </div>
  </section>

</main>
</body>
</html>
```